Executive search firm in fashion, luxury and retail industry needs logo and card design.

We are a start-up recruiting firm that specializes in the retail and fashion industry, based in New York. We are looking for something that will appeal to CEO level clients and candidates, but that has a little design edge...not overly corporate but still CEO-appropriate. We have clean, sophisticated taste and want a contemporary feel. Happy to have a two sided card. Not afraid of a little color but it should be high-design, not gimmicky and tasteful.

Quillby Market(s)

CEO's, HR Leaders, in retail, fashion (i.e. Havenmere, Quillby, Otto Vasquel)

Industry/Entity Type

Professional Service

Contact Information for Business Card

Linden Row Talent Partners
Address to be determined
Harlow Point, NY 10990

Marla Tovick
Managing Director
(555)013-2846
mtovick@lindenrowtalent.example

Font styles to use
Serif
Sans Serif

Requirements
Must have
• clean lines, crisp graphics, some color. Prefer a graphic treatment over a "logo" per se. No pictures, etc.
Nice to have
• double sided design.
Should not have
• Gimmicks, smaltz, goop. Think Gallery of Current Forms, not the Pelham Vault. No earth tones, as in beige and brown, no pastels. Strong colors are fine in moderation. Grays are good. Jewel tones are good. No red.

```html
<!DOCTYPE html>
<html lang="en">
<head>
<meta charset="utf-8">
<title>Linden Row Talent Partners — Business Card</title>
<link rel="stylesheet" href="https://fonts.googleapis.com/css2?family=Roboto+Slab:wght@500;700;800&display=swap">
<style>
  :root {
    --page-bg: #ececec;
    --teal: #0a4a62;
    --teal-deep: #073a4e;
    --gold: #e2b744;
    --gold-light: #f3d77f;
    --gold-dark: #b8862a;
    --white: #ffffff;
    --card-w: 840px;
    --card-h: 480px;
    --radius: 34px;
  }
  * { box-sizing: border-box; margin: 0; padding: 0; }
  html, body {
    width: 1200px;
    height: 1200px;
    overflow: hidden;
  }
  body {
    background: var(--page-bg);
    display: flex;
    flex-direction: column;
    align-items: center;
    justify-content: center;
    gap: 60px;
    font-family: "Roboto Slab", Georgia, serif;
  }
  .card {
    position: relative;
    width: var(--card-w);
    height: var(--card-h);
    border-radius: var(--radius);
    overflow: hidden;
    box-shadow: 0 10px 30px rgba(0, 0, 0, 0.12);
  }

  /* Front */
  .card-front { background: var(--white); }
  .card-front .pattern-field {
    position: absolute;
    inset: 0;
    background:
      linear-gradient(135deg, var(--gold-dark) 0%, var(--gold-light) 35%, var(--gold) 60%, var(--gold-dark) 100%);
    opacity: 0.85;
  }
  .card-front .name-plate {
    position: absolute;
    left: 50%;
    top: 50%;
    transform: translate(-50%, -50%);
    width: 540px;
    height: 150px;
    background: var(--teal);
    border-radius: 26px;
    display: flex;
    align-items: center;
    justify-content: center;
    padding: 0 24px;
  }
  .firm-name {
    color: var(--gold);
    font-weight: 700;
    font-size: 32px;
    letter-spacing: 0.2px;
    white-space: nowrap;
  }

  /* Back */
  .card-back { background: var(--teal); }
  .card-back .tonal-pattern {
    position: absolute;
    inset: 0;
    background: linear-gradient(160deg, var(--teal) 0%, var(--teal-deep) 100%);
  }
  .contact-list {
    position: absolute;
    left: 56px;
    top: 56px;
    list-style: none;
    display: flex;
    flex-direction: column;
    gap: 14px;
  }
  .contact-item {
    display: flex;
    align-items: center;
    gap: 14px;
    color: var(--white);
    font-weight: 700;
    font-size: 20px;
    white-space: nowrap;
  }
  .contact-icon { width: 20px; height: 20px; flex: none; }
  .person {
    position: absolute;
    right: 60px;
    top: 200px;
    text-align: right;
    color: var(--white);
  }
  .person-name {
    font-weight: 800;
    font-size: 34px;
    line-height: 1.1;
  }
  .person-title {
    font-weight: 700;
    font-size: 15px;
    letter-spacing: 1.5px;
    text-transform: uppercase;
    margin-top: 6px;
  }
</style>
</head>
<body>

  <section class="card card-front">
    <div class="pattern-field" role="img" aria-label="Gold foil geometric star pattern on white"></div>
    <div class="name-plate">
      <span class="firm-name">Linden Row Talent Partners</span>
    </div>
  </section>

  <section class="card card-back">
    <div class="tonal-pattern" role="img" aria-label="Subtle tonal teal star pattern"></div>

    <ul class="contact-list">
      <li class="contact-item">
        <svg class="contact-icon" viewBox="0 0 24 24" aria-hidden="true">
          <path fill="var(--gold)" d="M6.6 10.8a15.2 15.2 0 0 0 6.6 6.6l2.2-2.2a1 1 0 0 1 1-.25 11.4 11.4 0 0 0 3.6.57 1 1 0 0 1 1 1V20a1 1 0 0 1-1 1A17 17 0 0 1 3 4a1 1 0 0 1 1-1h3.5a1 1 0 0 1 1 1c0 1.25.2 2.45.57 3.6a1 1 0 0 1-.25 1z"/>
        </svg>
        <span>(555)013-2846</span>
      </li>
      <li class="contact-item">
        <svg class="contact-icon" viewBox="0 0 24 24" aria-hidden="true">
          <rect x="2" y="5" width="20" height="14" rx="2" fill="var(--gold)"/>
          <path d="M3 6.5l9 6.5 9-6.5" fill="none" stroke="var(--teal)" stroke-width="1.8"/>
        </svg>
        <span>mtovick@lindenrowtalent.example</span>
      </li>
      <li class="contact-item">
        <svg class="contact-icon" viewBox="0 0 24 24" aria-hidden="true">
          <path fill="var(--gold)" d="M12 3l9 8h-3v9h-4.5v-6h-3v6H6v-9H3z"/>
        </svg>
        <span>Harlow Point, NY 10990</span>
      </li>
    </ul>

    <div class="person">
      <div class="person-name">Marla Tovick</div>
      <div class="person-title">Managing Director</div>
    </div>
  </section>

</body>
</html>
```